need eczema bath soak label/bag

need you to recreate this please. ai file. recreate this exact image please. ...if you want a big tip, create some different styles.

Colors
0054AA
0677BA
7BADD7
CADEEF
E8F1F8

```html
<!DOCTYPE html>
<html lang="en">
<head>
<meta charset="UTF-8">
<title>The Ocean Healed — Bath Soak Pouch Label</title>
<link rel="stylesheet" href="https://fonts.googleapis.com/css2?family=Barlow+Semi+Condensed:wght@600&family=Poppins:wght@400;500;600&display=swap">
<style>
  :root {
    --backdrop: #b4b4af;
    --ink: #2c3b3d;
    --foil: #fbfbfb;
    --sea-light: #cfe7e8;
    --sea: #4fb0b4;
    --sea-deep: #2f8f97;
    --foam: #f1f2f0;
    --wet-sand: #d9cbb5;
    --sand: #d4b990;
    --sand-deep: #c9ac80;
  }
  * { margin: 0; padding: 0; box-sizing: border-box; }
  html, body {
    width: 1200px;
    height: 1108px;
    overflow: hidden;
    background: var(--backdrop);
  }
  .label {
    position: absolute;
    left: 195px;
    top: 34px;
    width: 810px;
    height: 1040px;
    overflow: hidden;
    background: var(--foil);
  }
  .label__scene {
    position: absolute;
    inset: 0;
    background: linear-gradient(
      to bottom,
      var(--foil) 0%,
      var(--foil) 14%,
      var(--sea-light) 22%,
      var(--sea) 30%,
      var(--sea-deep) 36%,
      var(--sea) 41%,
      var(--foam) 50%,
      var(--foam) 58%,
      var(--wet-sand) 64%,
      var(--sand) 72%,
      var(--sand-deep) 100%
    );
  }
  .label__text {
    position: absolute;
    left: 0;
    width: 100%;
    text-align: center;
    color: var(--ink);
  }
  .headline {
    font-family: "Barlow Semi Condensed", sans-serif;
    font-weight: 600;
    line-height: 1;
  }
  .headline--lead { top: 108px; font-size: 42px; }
  .headline--main {
    top: 152px;
    font-size: 96px;
    line-height: 84px;
  }
  .body-copy {
    top: 420px;
    font-family: "Poppins", sans-serif;
    font-weight: 500;
    font-size: 10.5px;
    line-height: 15px;
    text-transform: uppercase;
    letter-spacing: 0.2px;
  }
  .tagline {
    top: 510px;
    font-family: "Poppins", sans-serif;
    font-weight: 600;
    font-size: 18px;
    letter-spacing: 1px;
  }
  .batch {
    top: 538px;
    font-family: "Poppins", sans-serif;
    font-weight: 500;
    font-size: 25px;
    letter-spacing: 1px;
  }
  .variant {
    top: 590px;
    font-family: "Poppins", sans-serif;
    font-weight: 600;
    font-size: 11px;
    letter-spacing: 1px;
  }
  .brand {
    top: 770px;
    display: flex;
    flex-direction: column;
    align-items: center;
    gap: 26px;
  }
  .brand__mark {
    width: 48px;
    height: 48px;
    background: var(--ink);
  }
  .brand__name {
    font-family: "Poppins", sans-serif;
    font-weight: 600;
    font-size: 21px;
    letter-spacing: 6px;
    padding-left: 6px;
  }
  .footnote {
    top: 934px;
    font-family: "Poppins", sans-serif;
    font-weight: 600;
    font-size: 11px;
    letter-spacing: 1px;
  }
</style>
</head>
<body>
  <main class="label">
    <div class="label__scene" role="img" aria-label="Aerial photo of turquoise ocean waves breaking into white foam over a sandy beach"></div>

    <h1 class="label__text headline headline--lead">THE</h1>
    <p class="label__text headline headline--main">OCEAN<br>HEALED<br>MY A BAG</p>

    <p class="label__text body-copy">
      Lorem ipsum dolor sit amet, consectetuer<br>
      adipiscing elit, sed diam nonummy<br>
      nibh euismod tincidunt ut laoreet dolore<br>
      magna aliquam erat volutpat.
    </p>

    <p class="label__text tagline">OCEAN | IN A BAG</p>
    <p class="label__text batch">B77 6.1119</p>
    <p class="label__text variant">DArn SOOAK</p>

    <div class="label__text brand">
      <span class="brand__mark"></span>
      <span class="brand__name">TIDEWELL</span>
    </div>

    <p class="label__text footnote">lorem ipsum.</p>
  </main>
</body>
</html>
```